Accident Law Firm Billboard Bold Easy to See Car Accidents

We need a billboard design that can catch attention in a very crowed Car Accident lawyer market. We wish to feature the phone number (652) 318-4470 as the focus of the Bill Board. We are trying to get the phone number recognized and remembered by drivers. The law firm name is not as crucial to remember.
Basically, It's CAR ACCIDENT? Then (652) 318-4470. We are not married to any specific color scheme but it has to POP and catch attention.
So the Crucial elements are as follows:
1. Phone number (652) 318-4470
2. Words CAR ACCIDENT?
3. Firm Logo in lower portion or where appropriate. Firm Logo to be provided
4. We may want to try a Day Glow orange color, with White and Black added. An example of the color scheme shall be provided.
5. Possible "Catch Phrase" to be used, "It's Time Call 9"
Target Market(s)
Orlando Florida Car Accident victims
Industry/Entity Type
Law Firm
Requirements
Must have
- Easy to see phone number (652) 318-4470
- Catch attention
Nice to have
- I would like to have the sign visible in bright sunlight and it not too hard to immediately know what phone number is for
Should not have
- too many words
- No bold enough
- confusing fonts
- Unclear fonts

```html
<!DOCTYPE html>
<html lang="en">
<head>
<meta charset="utf-8">
<title>Marlowe Law Firm – Car Accident Billboard</title>
<link rel="stylesheet" href="https://fonts.googleapis.com/css2?family=Oswald:wght@500;700&display=swap">
<style>
  :root {
    --stage: #eef0f2;
    --paper: #ffffff;
    --ink: #111111;
    --orange: #e2581c;
    --orange-deep: #a8380c;
    --orange-dark: #5e1f06;
    --white: #ffffff;
  }
  * { margin: 0; padding: 0; box-sizing: border-box; }
  html, body {
    width: 1200px;
    height: 846px;
    overflow: hidden;
    background: var(--stage);
  }
  .stage {
    position: relative;
    width: 1200px;
    height: 846px;
    display: flex;
    align-items: center;
    justify-content: center;
  }
  .billboard {
    position: relative;
    width: 1100px;
    height: 340px;
    background: var(--paper);
    overflow: hidden;
    box-shadow: 0 10px 30px rgba(0,0,0,0.15);
  }
  .billboard__band {
    position: absolute;
    inset: 0;
    width: 100%;
    height: 100%;
  }
  .billboard__photo {
    position: absolute;
    left: 0;
    top: 128px;
    width: 250px;
    height: 212px;
    background: radial-gradient(ellipse at 50% 50%, #a9542a 0%, var(--orange-deep) 45%, var(--orange-dark) 100%);
  }
  .brand {
    position: absolute;
    left: 330px;
    top: 22px;
    font-family: "Oswald", sans-serif;
    font-weight: 700;
    color: var(--ink);
    line-height: 1;
    text-transform: uppercase;
  }
  .brand__name {
    display: block;
    font-size: 40px;
    letter-spacing: 1px;
  }
  .brand__sub {
    display: block;
    font-size: 17px;
    letter-spacing: 6px;
    margin-top: 4px;
  }
  .headline {
    position: absolute;
    left: 290px;
    top: 112px;
    font-family: "Oswald", sans-serif;
    font-weight: 700;
    color: var(--white);
    text-transform: uppercase;
    line-height: 1;
  }
  .headline__question {
    display: block;
    font-size: 104px;
    letter-spacing: 1px;
  }
  .headline__phone {
    display: block;
    font-size: 78px;
    margin-top: 6px;
    letter-spacing: 1px;
  }
</style>
</head>
<body>
  <main class="stage">
    <section class="billboard" aria-label="Car accident billboard">
      <svg class="billboard__band" viewBox="0 0 1100 340" preserveAspectRatio="none" aria-hidden="true">
        <defs>
          <linearGradient id="road" x1="0" y1="0" x2="1" y2="1">
            <stop offset="0" stop-color="#c8481a"/>
            <stop offset="0.6" stop-color="#b9461a"/>
            <stop offset="1" stop-color="#8e3410"/>
          </linearGradient>
        </defs>
        <polygon points="0,128 1100,44 1100,340 0,340" fill="url(#road)"/>
        <polygon points="0,128 1100,44 1100,56 0,140" fill="var(--orange)"/>
      </svg>
      <div class="billboard__photo" role="img" aria-label="Photo of a crashed car front, toned orange"></div>
      <div class="brand">
        <span class="brand__name">Marlowe</span>
        <span class="brand__sub">Law Firm P.C.</span>
      </div>
      <h1 class="headline">
        <span class="headline__question">Car Accident?</span>
        <span class="headline__phone">(652) 318-4470</span>
      </h1>
    </section>
  </main>
</body>
</html>
```